Website home page re-design

I have a brochure website www.baylorwick-suites.com that allows customers to buy my product (rent meeting room or work space by the hour/day, etc or sign up for virtual office services). The mechanical aspects of the site are done and working... I just want a different, more market "correct" image on the site built around my logo, tag line and them colors (royal blue and kelly green).

Industry/Entity Type

Product

```html
<!DOCTYPE html>
<html lang="en">
<head>
<meta charset="utf-8">
<title>Baylorwick Suites</title>
<link href="https://fonts.googleapis.com/css2?family=Open+Sans:wght@400;600;700&family=Oswald:wght@500&display=swap" rel="stylesheet">
<style>
:root{
  --royal:#1d3c8f;
  --navy:#17295e;
  --kelly:#1aa34a;
  --kelly-dark:#13863b;
  --ink:#333;
  --muted:#777;
  --light:#f4f6f9;
  --footer:#2f3236;
  --footer-dark:#222428;
  --icon-bg:#dde8f6;
}
*{box-sizing:border-box;margin:0;padding:0}
html,body{width:716px;height:1200px;overflow:hidden}
body{font-family:"Open Sans",Arial,sans-serif;color:var(--ink);background:#fff;font-size:11px}

.site-header{height:72px;position:relative;background:#fff}
.brand{position:absolute;left:22px;top:18px;display:flex;align-items:center;gap:8px}
.brand-dot{width:30px;height:30px;border-radius:50%;background:var(--royal)}
.brand-name{font-size:24px;font-weight:700;color:var(--royal)}
.contact-strip{position:absolute;right:22px;top:4px;font-size:8px;color:var(--muted);display:flex;gap:16px}
.nav{position:absolute;right:0;top:22px;width:440px}
.nav-row{display:flex;height:24px}
.nav-row a{flex:1;display:flex;align-items:center;justify-content:center;font-size:8px;font-weight:600;color:#fff;text-decoration:none}
.nav-main{background:var(--navy)}
.nav-main a.active{background:var(--royal)}
.nav-sub{background:var(--kelly)}

.hero{position:relative;height:400px;background:linear-gradient(180deg,#cfd6dc 0%,#9aa3ab 45%,#4b4f55 100%)}
.hero-caption{position:absolute;left:0;right:0;bottom:26px;text-align:center;color:#fff;background:rgba(20,25,35,.45);padding:14px 0 12px}
.hero-caption h1{font-size:22px;font-weight:700;color:#fff}
.hero-caption p{font-size:10px;color:#b8f0c8;line-height:1.5}
.dots{position:absolute;bottom:10px;left:50%;transform:translateX(-50%);display:flex;gap:6px}
.dots span{width:7px;height:7px;border-radius:50%;background:#fff;opacity:.6}
.dots span.on{background:var(--kelly);opacity:1}

.about{display:flex;gap:24px;padding:24px 22px;height:258px;background:var(--light)}
.about-text{flex:1.25}
.section-title{font-size:18px;font-weight:600;color:var(--ink);margin-bottom:4px}
.section-title b{color:var(--royal)}
.rule{width:60px;height:3px;background:var(--kelly);margin-bottom:12px}
.about-text p{font-size:9.5px;line-height:1.7;color:#555}
.call{margin-top:14px;font-style:italic;font-size:12px;color:var(--royal)}
.call strong{color:var(--kelly);font-size:15px;margin-left:6px}
.tour{flex:1}
.tour .section-title{color:var(--royal)}
.video{height:130px;position:relative;background:linear-gradient(160deg,#7a8894,#3b4550)}
.video-bar{position:absolute;left:0;right:0;bottom:0;height:14px;background:rgba(0,0,0,.7)}

.promo{height:104px;background:var(--kelly);display:flex;align-items:center;justify-content:space-between;padding:0 30px}
.promo p{color:#fff;font-size:15px;font-weight:700;line-height:1.4;width:420px}
.btn-dark{background:#1c1f24;color:#fff;font-size:13px;font-weight:600;padding:12px 26px}

.services{height:168px;padding:16px 22px 0;position:relative}
.arrows{position:absolute;right:22px;top:22px;display:flex;gap:2px}
.arrows span{width:13px;height:13px;background:#555}
.service-list{display:flex;justify-content:space-between;margin-top:4px}
.service{width:120px;text-align:center}
.service-icon{width:62px;height:62px;border-radius:50%;background:var(--icon-bg);margin:0 auto 8px;display:flex;align-items:center;justify-content:center}
.service span{font-size:10px;font-weight:600;color:var(--ink);line-height:1.3;display:block}

.site-footer{height:160px;background:var(--footer);display:flex;gap:20px;padding:18px 22px;color:#bbb}
.site-footer h3{font-size:11px;color:#fff;font-weight:600;margin-bottom:4px}
.site-footer .rule{width:40px;height:2px;margin-bottom:10px}
.col{flex:1;font-size:8.5px;line-height:1.8}
.col ul{list-style:none}
.quote{font-style:italic;line-height:1.6}
.quote-by{color:var(--kelly);margin-top:6px;font-weight:600}
.field{height:15px;background:#fff;margin-bottom:5px}
.field.tall{height:32px}
.submit{float:right;background:var(--royal);color:#fff;font-size:8px;padding:3px 8px}

.bottom-bar{height:20px;background:var(--footer-dark);display:flex;align-items:center;justify-content:space-between;padding:0 22px;font-size:8px;color:#999}
.social{display:flex;gap:4px}
.social span{width:12px;height:12px;background:#555}
</style>
</head>
<body>
<header class="site-header">
  <div class="brand"><span class="brand-dot"></span><span class="brand-name">Baylorwick</span></div>
  <div class="contact-strip"><span>&#9742; 800-555-0148</span><span>&#9993; www.baylorwick-suites.com</span></div>
  <nav class="nav">
    <div class="nav-row nav-main"><a class="active">Home</a><a>Dispute Resolution Center</a><a>Business &amp; Professional Center</a><a>My Account</a></div>
    <div class="nav-row nav-sub"><a>Video Conference Services</a><a>Our Services</a><a>Book An Event</a><a>Contact Us</a></div>
  </nav>
</header>

<section class="hero" role="img" aria-label="Photo of business professionals seated around a meeting table">
  <div class="hero-caption">
    <h1>Baylorwick Nashville is Open!</h1>
    <p>Visit Our Dispute Resolution Center, Business Professional Center.<br>Check Out Our Recent Meeting and Virtual Office Programs</p>
  </div>
  <div class="dots"><span class="on"></span><span></span><span></span></div>
</section>

<section class="about">
  <div class="about-text">
    <h2 class="section-title">About <b>Baylorwick</b></h2>
    <div class="rule"></div>
    <p>Baylorwick Suites is a full-service venue designed specifically to address the meeting needs of legal practitioners, mediators, paralegals, court reporters and other business professionals. Rent a room by the hour or day, book a virtual office, host a deposition or arbitration, and meet your clients in a quiet, well-equipped space.</p>
    <p class="call">Call Us Today <strong>800-555-0148</strong></p>
  </div>
  <div class="tour">
    <h2 class="section-title">Virtual Tour Vedio</h2>
    <div class="rule"></div>
    <div class="video" role="img" aria-label="Video still of a meeting room tour"><div class="video-bar"></div></div>
  </div>
</section>

<section class="promo">
  <p>Lorem ipsum dolor sit amet, consectetuer adipiscing elit, sed diam nonummy nibh euismod tincidunt ut laoreet</p>
  <span class="btn-dark">Book An Event</span>
</section>

<section class="services">
  <h2 class="section-title">Our <b>Services</b></h2>
  <div class="rule"></div>
  <div class="arrows"><span></span><span></span></div>
  <div class="service-list">
    <div class="service"><div class="service-icon"><svg width="30" height="30" viewBox="0 0 30 30"><path d="M4 15 15 5l11 10h-3v10h-6v-7h-4v7H7V15z" fill="#1d3c8f"/></svg></div><span>Work-From-Home Professionals</span></div>
    <div class="service"><div class="service-icon"><svg width="30" height="30" viewBox="0 0 30 30"><rect x="7" y="5" width="16" height="21" fill="#1d3c8f"/><rect x="10" y="8" width="3" height="3" fill="#dde8f6"/><rect x="17" y="8" width="3" height="3" fill="#dde8f6"/><rect x="10" y="14" width="3" height="3" fill="#dde8f6"/><rect x="17" y="14" width="3" height="3" fill="#dde8f6"/></svg></div><span>Real Estate Agents</span></div>
    <div class="service"><div class="service-icon"><svg width="30" height="30" viewBox="0 0 30 30"><path d="M3 15a12 10 0 0 1 24 0z" fill="#1d3c8f"/><path d="M15 15v9a2 2 0 0 1-4 0" stroke="#1d3c8f" stroke-width="2" fill="none"/></svg></div><span>Insurance Agents</span></div>
    <div class="service"><div class="service-icon"><svg width="30" height="30" viewBox="0 0 30 30"><rect x="8" y="5" width="12" height="7" transform="rotate(-35 14 8)" fill="#1d3c8f"/><path d="M16 13 24 24" stroke="#1d3c8f" stroke-width="3"/><rect x="4" y="24" width="12" height="3" fill="#1d3c8f"/></svg></div><span>Court Reporters</span></div>
    <div class="service"><div class="service-icon"><svg width="30" height="30" viewBox="0 0 30 30"><rect x="7" y="6" width="16" height="20" rx="1" fill="#1d3c8f"/><rect x="11" y="4" width="8" height="4" fill="#17295e"/><path d="M10 13h10M10 17h10M10 21h6" stroke="#dde8f6" stroke-width="1.5"/></svg></div><span>Claims Adjusters</span></div>
  </div>
</section>

<footer class="site-footer">
  <div class="col">
    <h3>Client Testimonials</h3><div class="rule"></div>
    <p class="quote">"Clean rooms, friendly staff and easy booking. Our depositions ran smoothly and our clients felt right at home every visit."</p>
    <p class="quote-by">Mara Ellison<br><span style="color:#bbb;font-weight:400">Business Man</span></p>
  </div>
  <div class="col">
    <h3>Quick Links</h3><div class="rule"></div>
    <ul><li>› Home</li><li>› Video Conference Services</li><li>› Our Services</li><li>› Book An Event</li><li>› Contact Us</li></ul>
  </div>
  <div class="col">
    <h3>Get in Touch</h3><div class="rule"></div>
    <p>1450 Harbor Lane<br>Nashville TN 37217</p>
    <p>&#9742; 800-555-0148</p>
    <p>&#9993; info@baylorwick-suites.com</p>
    <p>Mon-Fri : 9 am to 5 pm<br>Sat-Sun : Closed</p>
  </div>
  <div class="col">
    <h3>Leave us a Message</h3><div class="rule"></div>
    <div class="field"></div><div class="field"></div><div class="field tall"></div>
    <span class="submit">SUBMIT</span>
  </div>
</footer>
<div class="bottom-bar"><span>© Baylorwick 2024. All Rights Reserved</span><div class="social"><span></span><span></span><span></span><span></span></div></div>
</body>
</html>
```